Icons for Buttons of Time Clock Kiosk

Create Icons for 6 buttons of a screen of a computer screen used by employees to record their work.
In the icons I am looking for different icon for each button.
The icon should contain an image that will be associated with its action.
For example "Start lunch" will have food.
The kiosks are used in agriculture mainly in packing houses.
An employee clicks those buttons when he starts the work day,
leave for break,
returns from break,
leaves for lunch,
returns from lunch,
and finishes the work day.
Agricultural Packing Facilities
Agriculture

```html
<!DOCTYPE html>
<html lang="en">
<head>
<meta charset="utf-8">
<title>Time Clock Kiosk Buttons</title>
<link href="https://fonts.googleapis.com/css2?family=Jost:wght@700&display=swap" rel="stylesheet">
<style>
  :root {
    --bg: #ffffff;
    --label: #ffffff;
    --time-in-a: #ff3d45; --time-in-b: #d92ef5;
    --time-out-a: #7eff6a; --time-out-b: #8c9ab0; --time-out-c: #8428f8;
    --start-break-a: #8a2ef5; --start-break-b: #c67a8a; --start-break-c: #fdb62a;
    --end-break-a: #fc2ef5; --end-break-b: #ff7a8a; --end-break-c: #ffb52e;
    --start-lunch-a: #b8148c; --start-lunch-b: #7a5ac8; --start-lunch-c: #2e9cfe;
    --end-lunch-a: #1a7dd6; --end-lunch-b: #a986ec; --end-lunch-c: #fa82f8;
  }
  html, body {
    margin: 0;
    width: 1200px;
    height: 1000px;
    overflow: hidden;
    background: var(--bg);
  }
  .kiosk-panel {
    position: relative;
    width: 1200px;
    height: 1000px;
  }
  .clock-button {
    position: absolute;
    width: 329px;
    height: 135px;
    border-radius: 37px;
    display: flex;
    align-items: center;
    justify-content: center;
    gap: 12px;
    font-family: "Jost", "Futura", sans-serif;
    font-weight: 700;
    font-size: 37px;
    letter-spacing: 1.2px;
    white-space: nowrap;
    color: var(--label);
  }
  .action-icon {
    width: 32px;
    height: 32px;
    flex: none;
    fill: none;
    stroke: var(--label);
    stroke-width: 2.4;
    stroke-linecap: round;
    stroke-linejoin: round;
  }
  .col-left { left: 211px; }
  .col-right { left: 672px; }
  .row-1 { top: 243px; }
  .row-2 { top: 441px; }
  .row-3 { top: 640px; }
  .time-in { background: linear-gradient(90deg, var(--time-in-a) 5%, var(--time-in-b) 95%); }
  .time-out { background: linear-gradient(90deg, var(--time-out-a) 3%, var(--time-out-b) 50%, var(--time-out-c) 95%); }
  .start-break { background: linear-gradient(90deg, var(--start-break-a) 5%, var(--start-break-b) 55%, var(--start-break-c) 97%); }
  .end-break { background: linear-gradient(90deg, var(--end-break-a) 3%, var(--end-break-b) 50%, var(--end-break-c) 92%); }
  .start-lunch { background: linear-gradient(90deg, var(--start-lunch-a) 12%, var(--start-lunch-b) 50%, var(--start-lunch-c) 97%); }
  .end-lunch { background: linear-gradient(90deg, var(--end-lunch-a) 5%, var(--end-lunch-b) 55%, var(--end-lunch-c) 95%); }
</style>
</head>
<body>
  <main class="kiosk-panel">
    <div class="clock-button time-in col-left row-1">
      <svg class="action-icon" viewBox="0 0 24 24" aria-hidden="true">
        <path d="M14 4h4a2 2 0 0 1 2 2v12a2 2 0 0 1-2 2h-4"/>
        <path d="M4 12h11"/><path d="M11 8l4 4-4 4"/>
      </svg>
      <span>Time In</span>
    </div>
    <div class="clock-button time-out col-right row-1">
      <svg class="action-icon" viewBox="0 0 24 24" aria-hidden="true">
        <path d="M10 4H6a2 2 0 0 0-2 2v12a2 2 0 0 0 2 2h4"/>
        <path d="M10 12h10"/><path d="M16 8l4 4-4 4"/>
      </svg>
      <span>Time Out</span>
    </div>
    <div class="clock-button start-break col-left row-2">
      <svg class="action-icon" viewBox="0 0 24 24" aria-hidden="true">
        <path d="M3 9h13v5a5 5 0 0 1-5 5H8a5 5 0 0 1-5-5z"/>
        <path d="M16 10h2a2 2 0 0 1 0 4h-2"/>
        <path d="M7.5 3v3M11.5 3v3"/>
      </svg>
      <span>Start Break</span>
    </div>
    <div class="clock-button end-break col-right row-2">
      <svg class="action-icon" viewBox="0 0 24 24" aria-hidden="true">
        <path d="M3 9h13v5a5 5 0 0 1-5 5H8a5 5 0 0 1-5-5z"/>
        <path d="M16 10h2a2 2 0 0 1 0 4h-2"/>
        <path d="M6.5 13.5l2.5 2.5 4-4.5"/>
      </svg>
      <span>End Break</span>
    </div>
    <div class="clock-button start-lunch col-left row-3">
      <svg class="action-icon" viewBox="0 0 24 24" aria-hidden="true">
        <path d="M5 3v6a2.5 2.5 0 0 0 5 0V3"/>
        <path d="M7.5 3v18"/>
        <path d="M18 21V3c-2.2 1.5-3.5 4-3.5 7v3H18"/>
      </svg>
      <span>Start Lunch</span>
    </div>
    <div class="clock-button end-lunch col-right row-3">
      <svg class="action-icon" viewBox="0 0 24 24" aria-hidden="true">
        <circle cx="12" cy="12" r="9"/>
        <path d="M8 12.5l3 3 5-6"/>
      </svg>
      <span>End Lunch</span>
    </div>
  </main>
</body>
</html>
```